House Builder and Property Development Card Design and Logo

I need a business card design for a building and property development company.
Colour scheme of Dark Grey and Green, I would like it bold, sharp and professional.
No logo yet done, I'm open to options but please stay away from the usual- house, roof, hammers etc.
Thanks Rob

Please be aware that on the business card information section the WHRC # 5528391 is a licence number and my phone number 0492837165. The numbers are close together and could be mistaken as one whole number 

Thank you

                                   

Industry/Entity Type

Building

Contact Information for Business Card

VARGA BUILD & DEVELOPMENT.
Residential Building & Property Development
Robert Varga - Director
WHRC # 5528391
0492837165
rob@vargabuild.example.com.au

Requirements
Must have
• Bold Business name
Dark grey and green colours
Should not have
• roof outline or hammer logo

```html
<!DOCTYPE html>
<html lang="en">
<head>
<meta charset="utf-8">
<title>Varga Build &amp; Development – Business Cards</title>
<link href="https://fonts.googleapis.com/css2?family=Open+Sans:ital,wght@0,300;0,400;0,600;0,700;1,400&display=swap" rel="stylesheet">
<style>
  :root {
    --grey: #5f5a58;
    --grey-dark: #555050;
    --green: #0b9444;
    --green-deep: #0b7138;
    --ink: #1d1d1b;
    --white: #ffffff;
    --frame: #9a9a9a;
  }
  * { box-sizing: border-box; margin: 0; padding: 0; }
  html, body { width: 1200px; height: 832px; overflow: hidden; background: var(--white); }
  body { font-family: "Open Sans", Arial, sans-serif; }

  .sheet {
    position: relative;
    width: 1200px; height: 832px;
    border: 1px solid var(--frame);
    background: var(--white);
  }
  .card { position: absolute; width: 536px; height: 331px; overflow: hidden; }

  /* Front, diagonal variant */
  .card--diagonal { left: 46px; top: 55px; background: var(--grey); }
  .card--diagonal .diagonal { position: absolute; inset: 0; width: 100%; height: 100%; }

  /* Front, split variant */
  .card--split { left: 57px; top: 449px; background: var(--white); }
  .split-top { position: absolute; left: 0; top: 0; width: 100%; height: 210px; background: var(--green-deep); }
  .split-bottom { position: absolute; left: 0; top: 214px; width: 100%; height: 117px; background: var(--grey); }

  /* Backs */
  .card--brand { background: var(--white); border: 1.5px solid var(--frame); }
  .card--brand-centred { left: 619px; top: 59px; }
  .card--brand-offset { left: 630px; top: 449px; }

  .person { position: absolute; color: var(--white); }
  .person__name { font-weight: 700; font-size: 29px; line-height: 1; letter-spacing: -0.2px; }
  .person__role { display: block; text-align: right; color: var(--ink); font-weight: 700; font-size: 17px; line-height: 1; margin-top: 1px; }

  .phone { position: absolute; color: var(--white); }
  .phone__number { font-weight: 300; font-size: 35px; line-height: 1; letter-spacing: 0.3px; }
  .phone__label { font-size: 14px; line-height: 1; margin-top: 2px; letter-spacing: 0.3px; }

  .licence { position: absolute; color: var(--white); text-align: right; }
  .licence__number { font-weight: 400; font-size: 20px; line-height: 1; }
  .licence__label { font-weight: 700; font-size: 11px; line-height: 1; margin-top: 4px; }

  .email { position: absolute; color: var(--white); font-style: italic; font-size: 20px; line-height: 1; }

  .company-name {
    position: absolute;
    color: var(--grey-dark);
    font-weight: 600;
    font-size: 40px;
    line-height: 1.15;
    letter-spacing: 0.5px;
  }
  .card--brand-centred .company-name { left: 0; right: 0; top: 120px; text-align: center; }
  .card--brand-offset .company-name { left: 60px; right: 30px; top: 120px; text-align: left; }
</style>
</head>
<body>
<main class="sheet">

  <section class="card card--diagonal" aria-label="Business card front, diagonal layout">
    <svg class="diagonal" viewBox="0 0 369 227" preserveAspectRatio="none" aria-hidden="true">
      <polygon points="369,42 369,227 0,227 0,220" fill="#ffffff"/>
      <polygon points="369,51 369,227 10,227" fill="#0b9444"/>
    </svg>
    <div class="person" style="left:32px; top:24px;">
      <p class="person__name">Robert Varga</p>
      <span class="person__role">Director</span>
    </div>
    <div class="phone" style="left:32px; top:150px;">
      <p class="phone__number">0492837165</p>
      <p class="phone__label">CONTACT NO.</p>
    </div>
    <div class="licence" style="right:34px; top:216px;">
      <p class="licence__number">WHRC # 5528391</p>
      <p class="licence__label">LICENCE #</p>
    </div>
    <p class="email" style="right:34px; top:274px;">rob@vargabuild.example.com.au</p>
  </section>

  <section class="card card--brand card--brand-centred" aria-label="Business card back, centred name">
    <p class="company-name">VARGA<br>BUILD &amp; DEVELOPMENT</p>
  </section>

  <section class="card card--split" aria-label="Business card front, split layout">
    <div class="split-top"></div>
    <div class="split-bottom"></div>
    <div class="person" style="left:33px; top:32px;">
      <p class="person__name">Robert Varga</p>
      <span class="person__role">Director</span>
    </div>
    <p class="email" style="right:131px; top:176px;">rob@vargabuild.example.com.au</p>
    <div class="phone" style="left:33px; top:250px;">
      <p class="phone__number">0492837165</p>
      <p class="phone__label">CONTACT NO.</p>
    </div>
    <div class="licence" style="right:34px; top:257px;">
      <p class="licence__number">WHRC # 5528391</p>
      <p class="licence__label">LICENCE #</p>
    </div>
  </section>

  <section class="card card--brand card--brand-offset" aria-label="Business card back, offset name">
    <p class="company-name">VARGA<br>BUILD &amp; DEVELOPMENT</p>
  </section>

</main>
</body>
</html>
```